Corridor Works

Small ageny public transit advocacy, funding and compliance.
Consulting and lobbying efforts for small public transit agencies and communities exploring public transit opportunities.

I was interested in a simple line sketch suggesting motion, mobility. The card will be black on white. I would like it to include the bUs ones brief; Advocacy, Funding , and Compliance for small transit agencies.

Reason: I have been traveling and have had limited time to respond. Thank you all for your submit talks.

Industry/Entity Type

Consulting

Contact Information for Business Card

Paul R Vesby
Phone (907) 418-2960
Email paulrvesby@mailnook.net

```html
<!DOCTYPE html>
<html lang="en">
<head>
<meta charset="utf-8">
<title>Corridor Works – Business Card</title>
<link rel="stylesheet" href="https://fonts.googleapis.com/css2?family=Archivo:wght@400;900&display=swap">
<style>
  :root {
    --page-bg: #d9d9d9;
    --card-bg: #ffffff;
    --brand-green: #7dc21e;
    --ink: #111111;
    --card-shadow: rgba(0, 0, 0, 0.22);
  }
  * { box-sizing: border-box; margin: 0; padding: 0; }
  html, body {
    width: 1200px;
    height: 787px;
    overflow: hidden;
  }
  body {
    background: var(--page-bg);
    font-family: "Archivo", Arial, sans-serif;
    color: var(--ink);
  }
  .business-card {
    position: absolute;
    left: 160px;
    top: 143px;
    width: 880px;
    height: 500px;
    background: var(--card-bg);
    overflow: hidden;
    box-shadow: 0 6px 18px var(--card-shadow);
  }
  .accent-stripe {
    position: absolute;
    left: 0;
    top: 0;
    width: 20px;
    height: 100%;
    background: var(--brand-green);
  }
  .company-name {
    position: absolute;
    left: 92px;
    top: 40px;
    font-weight: 900;
    font-size: 44px;
    line-height: 0.95;
    letter-spacing: 0.5px;
    text-transform: uppercase;
    color: var(--ink);
  }
  .person-name {
    position: absolute;
    left: 92px;
    top: 170px;
    font-weight: 400;
    font-size: 36px;
    letter-spacing: 0.5px;
  }
  .contact-list {
    position: absolute;
    left: 80px;
    top: 250px;
    list-style: none;
    font-size: 21px;
    line-height: 1.3;
  }
  .contact-item {
    display: flex;
    align-items: flex-start;
    margin-bottom: 16px;
  }
  .contact-icon {
    width: 28px;
    height: 24px;
    margin-right: 14px;
    flex-shrink: 0;
    fill: var(--brand-green);
  }
  .vehicle-art {
    position: absolute;
    left: 560px;
    top: 48px;
    width: 320px;
    height: 452px;
    background: var(--brand-green);
    border-radius: 60px 0 0 0;
  }
  .service-list {
    position: absolute;
    left: 610px;
    top: 92px;
    width: 230px;
    padding: 14px 18px;
    background: var(--card-bg);
    border-radius: 10px;
    list-style: none;
    font-size: 20px;
    line-height: 1.4;
  }
  .service-list li::before {
    content: "";
    display: inline-block;
    width: 7px;
    height: 7px;
    margin-right: 6px;
    border-radius: 50%;
    background: var(--brand-green);
    vertical-align: middle;
  }
</style>
</head>
<body>
  <article class="business-card">
    <div class="accent-stripe"></div>

    <h1 class="company-name">Corridor<br>Works</h1>
    <p class="person-name">Paul R Vesby</p>

    <ul class="contact-list">
      <li class="contact-item">
        <svg class="contact-icon" viewBox="0 0 28 24" aria-hidden="true">
          <path d="M9 2h4l1 5-3 2c1 3 3 5 6 6l2-3 5 1v4c0 2-1 3-3 3C12 20 4 12 4 5c0-2 1-3 2-3z" transform="translate(-1 0) scale(0.95)"/>
        </svg>
        <span>(907) 418-2960</span>
      </li>
      <li class="contact-item">
        <svg class="contact-icon" viewBox="0 0 28 24" aria-hidden="true">
          <rect x="1" y="4" width="26" height="17" rx="1"/>
          <path d="M2 5l12 9 12-9" fill="none" stroke="#fff" stroke-width="2"/>
        </svg>
        <span>paulrvesby@mailnook.net</span>
      </li>
      <li class="contact-item">
        <svg class="contact-icon" viewBox="0 0 28 24" aria-hidden="true">
          <path d="M14 2L1 13h4v9h7v-6h4v6h7v-9h4z"/>
        </svg>
        <span>318C Harbor Ridge Ave.<br>Juneau, AK 99802</span>
      </li>
    </ul>

    <div class="vehicle-art" role="img" aria-label="Green front-view bus illustration"></div>
    <ul class="service-list">
      <li>Advocacy</li>
      <li>Funding</li>
      <li>Compliance</li>
    </ul>
  </article>
</body>
</html>
```